Flat bootstrap design for existing site

I'm looking for a modern flat design based around an existing logo. This has to be a custom design (no external templates), and implemented into a bootstrap framework.

The logo is attached as 2 versions - choose whichever you want, that flows better with whatever design you choose.

Added screenshots of the existing site (currently using the default bootstrap layouts). Please make your designs around those pages in the screenshots (i.e. the homepage only has the postal code input and the header). The active page has 3 screenshots, because I wanted to illustrate the other states that would be visible (in the table rows).

This is a moving/junk removal website, just for some context.

Here's some example websites (flat designs) that I like, just to give you an idea of what I'm after.

https://www.plivento.com/
https://hoskadel.com/
https://trumvex.com/
https://bravolinth.com/en/

• It must be a modern/simple flat design, that is built around the existing logo (attached).
• It has to be implemented using bootstrap.

```html
<!DOCTYPE html>
<html lang="en">
<head>
<meta charset="utf-8">
<title>HAULMOO – Sign In</title>
<link rel="stylesheet" href="https://fonts.googleapis.com/css2?family=Montserrat:wght@600;700&family=Roboto:wght@500&family=Mulish:wght@400&display=swap">
<style>
  :root {
    --sky: #38bdf2;
    --sky-light: #8fd6f6;
    --sky-hill: #7ccef4;
    --purple: #625bc6;
    --title: #5a55a8;
    --driver-blue: #0d84cc;
    --white: #ffffff;
    --input-border: #d8d8e2;
    --placeholder: #8a8a99;
    --footer-text: #3d3d5c;
    --social: #8f8bb8;
  }
  * { box-sizing: border-box; margin: 0; padding: 0; }
  html, body { width: 1200px; height: 658px; overflow: hidden; }
  body { position: relative; background: var(--white); font-family: "Mulish", sans-serif; }

  .hero { position: absolute; left: 0; top: 0; width: 1200px; height: 593px; background: var(--sky); overflow: hidden; }

  .brand { position: absolute; left: 144px; top: 22px; display: flex; align-items: center; gap: 8px;
    font-family: "Montserrat", sans-serif; font-weight: 700; font-size: 28px; color: var(--white); letter-spacing: 1px; }
  .brand-dot { width: 12px; height: 12px; border-radius: 50%; background: var(--white); }

  .nav { position: absolute; top: 22px; right: 144px; display: flex; align-items: center;
    font-family: "Montserrat", sans-serif; font-weight: 700; font-size: 11px; letter-spacing: .6px; color: var(--white); }
  .nav-link { margin-right: 26px; }
  .nav-link + .nav-link { margin-right: 24px; }
  .nav-btn { height: 35px; padding: 0 12px; display: flex; align-items: center; border-radius: 2px; }
  .nav-btn.driver { background: var(--driver-blue); margin-right: 8px; width: 135px; justify-content: center; }
  .nav-btn.signin { background: var(--purple); width: 81px; justify-content: center; }

  .signin-card { position: absolute; left: 396px; top: 132px; width: 408px; height: 342px; background: var(--white);
    border-radius: 3px; box-shadow: 0 6px 18px rgba(20, 80, 130, .18); }
  .signin-title { position: absolute; top: 176px; left: 0; width: 1200px; }
  .signin-card h1 { margin-top: 47px; text-align: center; font-family: "Roboto", sans-serif; font-weight: 500;
    font-size: 24px; color: var(--title); }
  .field { position: absolute; left: 37px; width: 333px; height: 52px; border: 1px solid var(--input-border);
    border-radius: 2px; padding-left: 15px; display: flex; align-items: center; font-size: 12.5px; color: var(--placeholder); }
  .field.email { top: 95px; }
  .field.password { top: 155px; }
  .forgot { position: absolute; right: 37px; top: 213px; font-size: 10.5px; color: var(--purple); }
  .login-btn { position: absolute; left: 37px; top: 239px; width: 333px; height: 52px; background: var(--purple);
    border-radius: 2px; display: flex; align-items: center; justify-content: center;
    font-family: "Montserrat", sans-serif; font-weight: 700; font-size: 17px; letter-spacing: 1.5px; color: var(--white); }

  .hill { position: absolute; left: 1008px; top: 440px; width: 420px; height: 420px; border-radius: 50%;
    background: var(--sky-hill); opacity: .75; }
  .driver-scene { position: absolute; left: 1048px; top: 432px; width: 152px; height: 112px; border-radius: 6px;
    background: linear-gradient(135deg, #5aa9e0, #3e8fd4 60%, #9ad07a); opacity: .85; }

  .footer { position: absolute; left: 0; top: 593px; width: 1200px; height: 58px; background: var(--white); }
  .copyright { position: absolute; left: 144px; top: 23px; font-size: 12.5px; color: var(--footer-text); }
  .social { position: absolute; right: 144px; top: 17px; display: flex; gap: 6px; }
  .social span { width: 19px; height: 19px; border-radius: 2px; background: var(--social); }
  .footer-band { position: absolute; left: 0; top: 651px; width: 1200px; height: 7px; background: var(--purple); }
</style>
</head>
<body>
  <section class="hero">
    <div class="brand"><span class="brand-dot"></span>HAULMOO</div>
    <nav class="nav">
      <span class="nav-link">BOOK</span>
      <span class="nav-link">HOW IT WORKS</span>
      <span class="nav-btn driver">BECOME A DRIVER</span>
      <span class="nav-btn signin">SIGNIN</span>
    </nav>

    <div class="hill"></div>
    <div class="driver-scene" role="img" aria-label="Illustration of a mover with a bin, bags, a house and a branded van"></div>

    <form class="signin-card">
      <h1>Please Sign In</h1>
      <div class="field email">Email</div>
      <div class="field password">Password</div>
      <span class="forgot">Forgot your password?</span>
      <div class="login-btn">LOGIN</div>
    </form>
  </section>

  <footer class="footer">
    <p class="copyright">© 2017 HAULMOO. All rights reserved.</p>
    <div class="social"><span></span><span></span><span></span></div>
  </footer>
  <div class="footer-band"></div>
</body>
</html>
```